Redesign of the Klammbrot label

I am a pharmacist and sell a bitters called "Klammbrot". I would like to revise and modernize the current logo of my "Klammbrot". I have attached a photo of the current label. I have different bottle sizes with different label sizes, but for now I will only need one label for the 700ml size:
20ml 36x47mm
40ml 45x62mm
200ml 70x91mm
350ml 70x98mm
500ml 70x110mm
700ml 87x119mm
The Uffe is a small stream that runs through our town. The Klammbrot is a play on words that takes up the mysticism of the Harz, as a spirit can of course also be a schnapps. I like the mysticism and rough nature of the Harz in connection with the product. I have attached a logo suggestion that I once had an AI design. But I am very open to new ideas. A connection to my pharmacy does not necessarily have to be recognizable. VG, K. Brandis

Target Market(s)

End consumers, gastronomy, restaurants, hotels

```html
<!DOCTYPE html>
<html lang="de">
<head>
<meta charset="utf-8">
<title>Klammbrot Bitterlikör – Etikett 700 ml</title>
<link rel="stylesheet" href="https://fonts.googleapis.com/css2?family=Oswald:wght@500;600&family=Montserrat:wght@400;600&display=swap">
<style>
  :root {
    --page: #f3f1ea;
    --cream: #f1efd3;
    --cream-deep: #e2e1bb;
    --green: #3f7b3b;
    --green-light: #7fb453;
    --maroon: #6e2428;
    --ink: #3b2c26;
  }
  * { box-sizing: border-box; margin: 0; padding: 0; }
  html, body { width: 900px; height: 1200px; overflow: hidden; background: var(--page); }
  .label {
    position: absolute; left: 140px; top: 40px; width: 620px; height: 1120px;
    background: radial-gradient(ellipse at 50% 35%, var(--cream) 40%, var(--cream-deep) 100%);
    border-radius: 310px 310px 18px 18px / 300px 300px 18px 18px;
    overflow: hidden;
    font-family: "Montserrat", sans-serif; color: var(--ink);
    box-shadow: 0 4px 18px rgba(0,0,0,.12);
  }
  .label-frame {
    position: absolute; left: 20px; top: 20px; right: 20px; bottom: 120px;
    border: 2px solid var(--maroon); border-bottom: none;
    border-radius: 290px 290px 0 0 / 280px 280px 0 0;
  }
  .herb-wreath {
    position: absolute; left: 40px; top: 40px; width: 540px; height: 470px;
    border-radius: 50%;
    background: radial-gradient(circle at 50% 48%, transparent 34%, rgba(95,140,80,.28) 46%, rgba(95,140,80,.08) 62%, transparent 72%);
  }
  .seal {
    position: absolute; left: 140px; top: 118px; width: 340px; height: 340px;
    border: 2px solid var(--maroon); border-radius: 50%;
    display: flex; align-items: center; justify-content: center;
  }
  .seal::before {
    content: ""; position: absolute; inset: 10px;
    border: 1px solid var(--maroon); border-radius: 50%;
  }
  .seal-core {
    width: 196px; height: 196px; border-radius: 50%;
    background: var(--green); border: 4px solid var(--maroon);
    display: flex; align-items: center; justify-content: center;
  }
  .seal-name {
    font-family: "Montserrat", sans-serif; font-weight: 600; font-size: 30px;
    letter-spacing: 1px; color: var(--cream);
  }
  .title-band {
    position: absolute; left: 22px; right: 22px; top: 513px; height: 136px;
    background: var(--green);
    border-top: 3px solid var(--maroon); border-bottom: 3px solid var(--maroon);
    display: flex; align-items: center; justify-content: center;
  }
  .title {
    font-family: "Oswald", sans-serif; font-weight: 600; font-size: 104px;
    line-height: 1; color: var(--cream); letter-spacing: 1px;
  }
  .tagline {
    position: absolute; left: 0; right: 0; top: 670px; text-align: center;
    font-weight: 600; font-size: 23px; color: var(--ink);
  }
  .dotted-rule {
    position: absolute; left: 50px; right: 40px; top: 712px;
    border-top: 4px dotted var(--maroon);
  }
  .description {
    position: absolute; left: 50px; right: 40px; top: 738px; text-align: center;
    font-size: 20px; line-height: 29px; color: var(--ink);
  }
  .solid-rule {
    position: absolute; left: 60px; right: 50px; top: 833px;
    border-top: 3px solid var(--maroon);
  }
  .facts {
    position: absolute; left: 50px; right: 40px; top: 848px; height: 115px;
    display: flex; align-items: flex-start;
  }
  .fact-volume, .fact-abv {
    font-family: "Oswald", sans-serif; font-weight: 600; font-size: 40px;
    line-height: 42px; color: var(--maroon); text-align: center;
  }
  .fact-volume { width: 100px; padding-top: 20px; }
  .fact-abv { width: 120px; padding-top: 18px; }
  .fact-origin {
    flex: 1; text-align: center; padding-top: 4px;
    border-left: 4px dotted var(--maroon); border-right: 4px dotted var(--maroon);
    height: 110px;
  }
  .origin-intro { font-size: 20px; line-height: 28px; }
  .origin-name { font-weight: 600; font-size: 21px; line-height: 28px; }
  .herb-meadow {
    position: absolute; left: 0; right: 0; bottom: 0; height: 185px;
    background: linear-gradient(to bottom, rgba(127,180,83,0) 0%, var(--green-light) 35%, #4d8a2e 100%);
  }
</style>
</head>
<body>
  <div class="label">
    <div class="herb-wreath" role="img" aria-label="Kranz aus gezeichneten Kräutern: Lavendel, Salbei, Minze und Zitronenmelisse"></div>
    <div class="label-frame"></div>
    <div class="seal">
      <div class="seal-core"><span class="seal-name">Klammbrot</span></div>
    </div>
    <div class="title-band"><h1 class="title">BITTERLIKÖR</h1></div>
    <p class="tagline">NACH ALTER APOTHEKERKUNST</p>
    <div class="dotted-rule"></div>
    <p class="description">Aufs Feinste zubereitet mit geistigen Auszugen<br>von Enzian, Kalmus, Malabar-Kardamom<br>und anderen wertvollen Zutaten.</p>
    <div class="solid-rule"></div>
    <div class="facts">
      <div class="fact-volume">700<br>ml</div>
      <div class="fact-origin">
        <p class="origin-intro">Aus der</p>
        <p class="origin-name">St. Veits Apotheke<br>Bad Harzfeld</p>
      </div>
      <div class="fact-abv">34%</div>
    </div>
    <div class="herb-meadow" role="img" aria-label="Foto frischer grüner Kräuterblätter am unteren Rand"></div>
  </div>
</body>
</html>
```